Infographic & Data Visualisation Design for – Australia’s Yearly Harmwatch Review 2026

About Carrowby Institute: Carrowby Institute is an independent non-profit public health organization. We produce Australia’s Yearly Harmwatch Review, which translates verified national mortality data into actionable insights for policymakers, journalists, healthcare workers, and the general public.

Project Goal: We need a suite of high-impact, clean, and authoritative infographics and data visualisations created for Australia’s Yearly Harmwatch Review 2026.

What We Are Providing:

Full Dataset (.xlsx): Complete Excel file containing all 2026 report data.

Data & Chart Guidance Doc (.docx): A summary document detailing each dataset, the core takeaway, and our initial recommendations for chart types (e.g., line graphs, horizontal bar charts, donut charts, metric tiles).

Carrowby Institute Brand Book (.pdf): Complete brand guidelines covering fonts, colors, line weights, and imagery. These guidelines and in particular colours should be used across the infographics.

Previous Year Reference: You can view how last year’s report and graphics here: https://www.carrowby-example.org.au/australias-yearly-harmwatch-review-2025/

Designer Input & Creative Freedom: While we have provided a guide suggesting specific chart types for each dataset, we are not data visualisation experts - you are! We are very open to your creative ideas, structural suggestions, and design expertise. If you identify a clearer, more engaging, or visually compelling way to illustrate a specific dataset, we welcome your input.

Required Deliverables:

Master Report Infographics: High-resolution, print/PDF-ready A4 vector graphics for the formal report publication (Delivered as vector AI/EPS and high-res PDF/PNG).

Web Assets: Web-optimized PNG/SVG files with transparent or brand backgrounds.

Social Media Adaptations: 1:1 (Square) and 4:5 / 9:16 (Vertical) graphic cards for Pictoral, WorkMesh, Chatterly, and X.
Updates

Deadline was too tight - have extended it to ensure the designers have enough time to do the job.

Target Market(s)

Policy makers, journalists, health sector professionals, frontline workers, and the general public.

Industry/Entity Type

Drug/Government/Not for Profit

Font styles to use
Sans Serif
Other font styles liked:
• Brand Fonts: Use any or a combination of: Host Grotesk or Libre Baskerville or Poppins or Calibri Light

Colors

Designer to choose colors to be used in the design.

Requirements
Must have
• The ability to create Infographics, graphs of all kinds from data that we have given.
Nice to have
• Help with choosing what infographics/graphs/donuts graphs etc will be best to visualise the data.
Should not have
• A designer who has not made graphs or infographics from Data.

```html
<!DOCTYPE html>
<html lang="en">
<head>
<meta charset="utf-8">
<title>Carrowby Institute – Yearly Harmwatch Review 2026 Infographics</title>
<link href="https://fonts.googleapis.com/css2?family=Host+Grotesk:wght@400;500;600;700;800&display=swap" rel="stylesheet">
<style>
:root{
  --board:#5f5f5f;
  --paper:#ffffff;
  --navy:#14274e;
  --blue:#438bcb;
  --grey:#9a9a9a;
  --faint:#eef0f3;
  --rule:#438bcb;
  --cell:#f3f5f8;
}
*{margin:0;padding:0;box-sizing:border-box}
html,body{width:1200px;height:1110px;overflow:hidden;background:var(--board)}
body{font-family:"Host Grotesk",Arial,sans-serif;color:var(--navy);position:relative}
.page{position:absolute;width:330px;height:466px;background:var(--paper);box-shadow:0 3px 10px rgba(0,0,0,.25);overflow:hidden}
.page--map{left:76px;top:71px}
.page--population{left:437px;top:71px}
.page--roadtoll{left:797px;top:71px}
.page--gender{left:76px;top:572px}
.page--age{left:437px;top:572px}
.abs{position:absolute}
.title{position:absolute;left:15px;top:14px;font-size:27px;line-height:26.5px;letter-spacing:-.2px}
.title .lt{color:var(--blue);font-weight:400}
.title .bd{color:var(--navy);font-weight:800}
.badge{position:absolute;left:15px;height:14px;padding:0 7px;background:var(--navy);color:#fff;font-size:7.5px;font-weight:600;line-height:14px;border-radius:2px}
.footer{position:absolute;left:15px;right:15px;top:425px;border-top:1px solid var(--rule)}
.footer .org{position:absolute;left:0;top:6px;font-size:10.5px;line-height:11px;font-weight:500;color:var(--navy)}
.footer .report{position:absolute;right:0;top:19px;font-size:6.5px;color:var(--navy)}
.footer .report b{color:var(--blue);font-weight:600}
.vpct{position:absolute;font-weight:800;transform:rotate(-90deg);transform-origin:center;white-space:nowrap;line-height:1}
/* page 1 */
.syringe-deco{left:200px;top:290px;width:100px;height:100px;background:var(--faint);border-radius:18px;transform:rotate(45deg)}
.map-area{left:41px;top:122px;width:246px;height:166px;background:var(--blue);border-radius:30% 38% 34% 26%}
.map-island{left:200px;top:270px;width:62px;height:76px;background:var(--blue);border-radius:0 0 40% 45%}
.map-total{left:0;width:330px;top:178px;text-align:center;font-size:38px;font-weight:800;color:var(--navy)}
.stat-tile{left:15px;top:311px;width:116px;height:87px;border:1px solid var(--navy);border-radius:4px;background:#fff;text-align:center}
.stat-tile .icon{display:block;margin:10px auto 0;width:26px;height:26px;background:var(--blue);border-radius:4px}
.stat-tile .sep{width:60px;height:1px;background:var(--blue);margin:5px auto 4px}
.stat-tile p{font-size:11.5px;line-height:12.5px}
.stat-tile b{color:var(--blue);font-weight:700}
/* page 2 */
.band{left:15px;top:164px;width:301px;height:90px;background:var(--blue);border-radius:6px 6px 0 0}
.card{background:#fff;border:1px solid var(--navy);border-radius:6px;box-shadow:0 2px 6px rgba(0,0,0,.12)}
.ptable{position:absolute;width:142px;font-size:7px;text-align:center}
.ptable .head{background:var(--navy);color:#fff;font-size:11px;font-weight:700;height:19px;line-height:19px}
.ptable .row{display:flex}
.ptable .row span{flex:1;background:var(--cell);margin:1px 1px 0 0;display:flex;align-items:center;justify-content:center}
.ptable .labels span{height:21px;color:var(--blue);line-height:7px}
.ptable .vals span{height:12px;color:var(--navy)}
/* page 3 */
.axis-title{left:15px;top:142px;font-size:7.5px;color:var(--blue)}
.legend{left:15px;top:320px;width:266px;height:71px;border:1px solid var(--navy);border-radius:4px;padding:11px 0 0 16px}
.legend li{list-style:none;font-size:11.5px;line-height:16.5px;display:flex;align-items:center}
.legend i{display:inline-block;width:24px;height:4px;margin-right:6px}
/* page 4 */
.gstat{position:absolute;line-height:1}
.gstat .pct{font-size:27px;font-weight:800;padding-bottom:2px;border-bottom:1px solid currentColor}
.gstat .lbl{font-size:10px;margin-top:3px}
.gstat .num{font-size:21px;margin-top:1px}
.gstat--m{left:28px;top:175px;color:var(--navy)}
.gstat--f{left:247px;top:175px;color:var(--blue)}
.gcard{position:absolute;top:293px;width:115px;height:108px;border-radius:4px;text-align:center}
.gcard--m{left:28px;border:1px solid var(--navy)}
.gcard--f{left:189px;border:1px solid var(--blue)}
.gcard .gicon{display:block;margin:12px auto 0}
.gcard .name{font-size:11.5px;font-weight:700;margin-top:3px}
.gcard .sep{width:80px;height:1px;background:var(--blue);margin:4px auto 0}
.gcard .yrs{display:flex;justify-content:space-between;padding:10px 10px 0;font-size:8px}
.gcard .flow{display:flex;justify-content:space-between;align-items:center;padding:3px 10px 0;font-size:11px;font-weight:700;line-height:1}
.gcard .flow svg{display:block}
.gdivider{position:absolute;left:166px;top:293px;height:108px;border-left:1px dashed var(--grey)}
</style>
</head>
<body>

<!-- Overdose deaths 2024 -->
<section class="page page--map">
  <h2 class="title"><span class="lt">Number of</span><br><span class="bd">overdose deaths</span> <span class="lt">in</span><br><span class="bd">Australia</span> <span class="lt">in</span> <span class="bd">2024</span></h2>
  <div class="abs syringe-deco" role="img" aria-label="Faint syringe and pill illustration"></div>
  <div class="abs map-area" role="img" aria-label="Map of Australia in brand blue"></div>
  <div class="abs map-island" role="img" aria-label="South-east of the Australia map"></div>
  <div class="abs map-total">2,596</div>
  <div class="abs stat-tile">
    <span class="icon" role="img" aria-label="Syringe and pills icon"></span>
    <div class="sep"></div>
    <p>All drug–induced<br>deaths <b>2,596</b></p>
  </div>
  <div class="vpct" style="left:123px;top:343px;font-size:25px">85%</div>
  <footer class="footer"><div class="org">CARROWBY<br>INSTITUTE</div><div class="report">Australia’s Yearly Harmwatch Review <b>2026</b></div></footer>
</section>

<!-- Population growth -->
<section class="page page--population">
  <h2 class="title"><span class="bd">Unintentional overdose</span><br><span class="bd">deaths</span> <span class="lt">compared with<br>population growth</span></h2>
  <div class="badge" style="top:104px">Australia 2001–2024</div>
  <div class="abs band"></div>
  <div class="abs card" style="left:15px;top:244px;width:300px;height:138px"></div>
  <div class="ptable" style="left:34px;top:309px">
    <div class="head">2024</div>
    <div class="row labels"><span>Population</span><span>Unintentional<br>overdose deaths</span></div>
    <div class="row vals"><span>27194300</span><span>2,091</span></div>
  </div>
  <svg class="abs" style="left:0;top:0" width="330" height="466" viewBox="0 0 330 466">
    <rect x="190" y="332" width="6" height="50" fill="var(--blue)"/><rect x="190" y="350" width="6" height="32" fill="var(--navy)"/>
    <polygon points="184,332 202,332 193,319" fill="var(--blue)"/>
    <rect x="213" y="312" width="7" height="70" fill="var(--blue)"/><rect x="213" y="337" width="7" height="45" fill="var(--navy)"/>
    <polygon points="205,312 228,312 216.5,297" fill="var(--blue)"/>
    <rect x="242" y="300" width="9" height="82" fill="var(--blue)"/><rect x="242" y="319" width="9" height="63" fill="var(--navy)"/>
    <polygon points="232,302 261,302 246.5,284" fill="var(--blue)"/>
    <rect x="275" y="285" width="11" height="97" fill="var(--blue)"/><rect x="275" y="302" width="11" height="80" fill="var(--navy)"/>
    <polygon points="263,287 298,287 280.5,265" fill="var(--blue)"/>
  </svg>
  <div class="vpct" style="left:283px;top:324px;font-size:13px">85%</div>

  <div class="abs card" style="left:30px;top:182px;width:206px;height:94px"></div>
  <div class="ptable" style="left:49px;top:203px">
    <div class="head">2001</div>
    <div class="row labels"><span>Population</span><span>Unintentional<br>overdose deaths</span></div>
    <div class="row vals"><span>19274700</span><span>981</span></div>
  </div>
  <svg class="abs" style="left:196px;top:200px" width="24" height="60" viewBox="0 0 24 60">
    <rect x="8" y="11" width="7" height="47" fill="var(--blue)"/>
    <rect x="8" y="42" width="7" height="16" fill="var(--navy)"/>
    <polygon points="2,13 21,13 11.5,1" fill="var(--blue)"/>
  </svg>
  <div class="vpct" style="left:213px;top:224px;font-size:13px">38%</div>
  <footer class="footer"><div class="org">CARROWBY<br>INSTITUTE</div><div class="report">Australia’s Yearly Harmwatch Review <b>2026</b></div></footer>
</section>

<!-- Road toll -->
<section class="page page--roadtoll">
  <h2 class="title"><span class="bd">Overdose deaths</span><br><span class="lt">compared with the</span><br><span class="bd">road toll</span></h2>
  <div class="badge" style="top:103px">Australia 2001–2024</div>
  <div class="abs axis-title">Number of Death</div>
  <svg class="abs" style="left:0;top:0" width="330" height="320" viewBox="0 0 330 320" font-family="Host Grotesk, Arial, sans-serif">
    <g stroke="#8a93a3" stroke-width=".6" stroke-dasharray="3 2">
      <line x1="41" y1="168" x2="315" y2="168"/><line x1="41" y1="193" x2="315" y2="193"/>
      <line x1="41" y1="218" x2="315" y2="218"/><line x1="41" y1="243" x2="315" y2="243"/>
      <line x1="41" y1="268" x2="315" y2="268"/>
    </g>
    <line x1="41" y1="164" x2="41" y2="294" stroke="var(--navy)" stroke-width=".7"/>
    <line x1="41" y1="294" x2="315" y2="294" stroke="var(--navy)" stroke-width=".7"/>
    <g font-size="8" fill="var(--navy)" text-anchor="end">
      <text x="37" y="171">3,000</text><text x="37" y="196">2,500</text><text x="37" y="221">2,000</text>
      <text x="37" y="246">1,500</text><text x="37" y="271">500</text><text x="17" y="296" text-anchor="start">0</text>
    </g>
    <rect x="81" y="233" width="15" height="61" fill="var(--grey)"/>
    <rect x="138" y="213" width="15" height="81" fill="var(--blue)"/>
    <rect x="199" y="186" width="15" height="108" fill="var(--navy)"/>
    <g font-size="8" text-anchor="middle">
      <text x="88.5" y="229" fill="var(--grey)">1307</text>
      <text x="145.5" y="208" fill="var(--blue)">2091</text>
      <text x="206.5" y="182" fill="var(--navy)">2596</text>
    </g>
    <polyline fill="none" stroke="var(--grey)" stroke-width=".8" points="44,291 59,291 74,285 88,284 105,277 121,277 141,270 168,263 185,263 216,256 249,249 264,242 296,235 312,235"/>
    <g fill="var(--grey)"><circle cx="59" cy="291" r="1.6"/><circle cx="74" cy="285" r="1.6"/><circle cx="105" cy="277" r="1.6"/><circle cx="121" cy="277" r="1.6"/><circle cx="168" cy="263" r="1.6"/><circle cx="185" cy="263" r="1.6"/><circle cx="216" cy="256" r="1.6"/><circle cx="249" cy="249" r="1.6"/><circle cx="264" cy="242" r="1.6"/><circle cx="296" cy="235" r="1.6"/><circle cx="312" cy="235" r="1.6"/></g>
    <polyline fill="none" stroke="var(--blue)" stroke-width=".8" points="44,284 61,283 79,276 105,274 124,261 138,261 153,260 167,250 185,251 200,240 229,239 249,226 271,228 291,215 312,215"/>
    <g fill="var(--blue)"><circle cx="61" cy="283" r="1.6"/><circle cx="105" cy="274" r="1.6"/><circle cx="124" cy="261" r="1.6"/><circle cx="167" cy="250" r="1.6"/><circle cx="185" cy="251" r="1.6"/><circle cx="229" cy="239" r="1.6"/><circle cx="249" cy="226" r="1.6"/><circle cx="271" cy="228" r="1.6"/><circle cx="291" cy="215" r="1.6"/><circle cx="312" cy="215" r="1.6"/></g>
    <polyline fill="none" stroke="var(--navy)" stroke-width=".8" points="44,279 65,275 81,269 96,260 107,261 124,243 138,245 153,245 167,229 188,233 199,233 206,216 232,219 249,202 272,205 291,187 312,186"/>
    <g fill="var(--navy)"><circle cx="65" cy="275" r="1.6"/><circle cx="107" cy="261" r="1.6"/><circle cx="124" cy="243" r="1.6"/><circle cx="167" cy="229" r="1.6"/><circle cx="188" cy="233" r="1.6"/><circle cx="232" cy="219" r="1.6"/><circle cx="249" cy="202" r="1.6"/><circle cx="272" cy="205" r="1.6"/><circle cx="291" cy="187" r="1.6"/><circle cx="312" cy="186" r="1.6"/></g>
    <g font-size="3.6" fill="var(--navy)" text-anchor="middle">
      <text x="43" y="305">2001</text><text x="55" y="305">2002</text><text x="66" y="305">2003</text><text x="78" y="305">2004</text><text x="90" y="305">2005</text><text x="102" y="305">2006</text><text x="114" y="305">2007</text><text x="126" y="305">2008</text><text x="138" y="305">2009</text><text x="149" y="305">2010</text><text x="161" y="305">2011</text><text x="173" y="305">2012</text><text x="185" y="305">2013</text><text x="197" y="305">2014</text><text x="209" y="305">2015</text><text x="221" y="305">2016</text><text x="232" y="305">2017</text><text x="244" y="305">2018</text><text x="256" y="305">2019</text><text x="268" y="305">2020</text><text x="280" y="305">2021</text><text x="292" y="305">2022</text><text x="303" y="305">2023</text><text x="314" y="305">2024</text>
    </g>
  </svg>
  <ul class="abs legend">
    <li><i style="background:var(--grey)"></i>All drug–induced deaths</li>
    <li><i style="background:var(--blue)"></i>Unintentional drug–induced deaths</li>
    <li><i style="background:var(--navy)"></i>Road traffic accident deaths</li>
  </ul>
  <footer class="footer"><div class="org">CARROWBY<br>INSTITUTE</div><div class="report">Australia’s Yearly Harmwatch Review <b>2026</b></div></footer>
</section>

<!-- Gender split -->
<section class="page page--gender">
  <h2 class="title"><span class="lt">Gender split of<br>unintentional</span><br><span class="bd">overdose deaths</span></h2>
  <div class="badge" style="top:97px">Australia 2001–2024</div>
  <svg class="abs" style="left:94px;top:135px" width="142" height="142" viewBox="0 0 142 142">
    <circle cx="71" cy="71" r="57" fill="none" stroke="var(--navy)" stroke-width="28"/>
    <circle cx="71" cy="71" r="57" fill="none" stroke="var(--blue)" stroke-width="28" stroke-dasharray="107.4 358.1" transform="rotate(-90 71 71)"/>
    <text x="71" y="67" font-size="7.5" text-anchor="middle" fill="var(--navy)" font-family="Host Grotesk, Arial, sans-serif">unintentional</text>
    <text x="71" y="75.5" font-size="7.5" text-anchor="middle" fill="var(--navy)" font-family="Host Grotesk, Arial, sans-serif">overdose deaths</text>
    <text x="71" y="84" font-size="7.5" text-anchor="middle" fill="var(--navy)" font-family="Host Grotesk, Arial, sans-serif">in <tspan fill="var(--blue)">2024</tspan></text>
  </svg>
  <div class="gstat gstat--m"><div class="pct">70%</div><div class="lbl">Males</div><div class="num">1520</div></div>
  <div class="gstat gstat--f"><div class="pct">30%</div><div class="lbl">Females</div><div class="num">571</div></div>
  <div class="gcard gcard--m">
    <svg class="gicon" width="30" height="30" viewBox="0 0 30 30"><circle cx="12" cy="18" r="8" fill="none" stroke="var(--blue)" stroke-width="3.2"/><path d="M18 12 L26 4 M19 4 H26 V11" fill="none" stroke="var(--blue)" stroke-width="3.2"/></svg>
    <div class="name" style="color:var(--blue)">Males</div><div class="sep"></div>
    <div class="yrs" style="color:var(--navy)"><span>2001</span><span>2024</span></div>
    <div class="flow" style="color:var(--navy)"><span>701</span><svg width="36" height="6" viewBox="0 0 36 6"><path d="M0 3 H34 M31 0.5 L34 3 L31 5.5" fill="none" stroke="var(--navy)" stroke-width="1"/></svg><span>1520</span></div>
  </div>
  <div class="gdivider"></div>
  <div class="gcard gcard--f">
    <svg class="gicon" width="30" height="30" viewBox="0 0 30 30"><circle cx="13" cy="17" r="9" fill="none" stroke="var(--navy)" stroke-width="3.2"/><path d="M21 4 L27 10 M27 4 L21 10" fill="none" stroke="var(--navy)" stroke-width="2.4"/></svg>
    <div class="name" style="color:var(--navy)">Females</div><div class="sep"></div>
    <div class="yrs" style="color:var(--blue)"><span>2001</span><span>2024</span></div>
    <div class="flow" style="color:var(--blue)"><span>280</span><svg width="36" height="6" viewBox="0 0 36 6"><path d="M0 3 H34 M31 0.5 L34 3 L31 5.5" fill="none" stroke="var(--blue)" stroke-width="1"/></svg><span>571</span></div>
  </div>
  <footer class="footer"><div class="org">CARROWBY<br>INSTITUTE</div><div class="report">Australia’s Yearly Harmwatch Review <b>2026</b></div></footer>
</section>

<!-- Age group -->
<section class="page page--age">
  <h2 class="title"><span class="lt">Percent of</span><br><span class="bd">unintentional overdose</span><br><span class="lt">deaths by age group</span></h2>
  <div class="badge" style="top:101px">Australia 2024</div>
  <svg class="abs" style="left:0;top:150px" width="330" height="230" viewBox="0 150 330 230" font-family="Host Grotesk, Arial, sans-serif">
    <line x1="61.5" y1="158" x2="61.5" y2="361" stroke="var(--navy)" stroke-width=".7"/>
    <line x1="61" y1="361" x2="308" y2="361" stroke="var(--navy)" stroke-width=".7"/>
    <g stroke="var(--navy)" stroke-width=".7">
      <line x1="61.5" y1="361" x2="61.5" y2="364"/><line x1="102.6" y1="361" x2="102.6" y2="364"/><line x1="143.8" y1="361" x2="143.8" y2="364"/><line x1="185" y1="361" x2="185" y2="364"/><line x1="226" y1="361" x2="226" y2="364"/><line x1="267" y1="361" x2="267" y2="364"/><line x1="308" y1="361" x2="308" y2="364"/>
    </g>
    <g font-size="6.5" fill="var(--navy)" text-anchor="middle">
      <text x="61.5" y="375">0%</text><text x="102.6" y="375">5%</text><text x="143.8" y="375">10%</text><text x="185" y="375">15%</text><text x="226" y="375">20%</text><text x="267" y="375">25%</text><text x="308" y="375">30%</text>
    </g>
    <g font-size="8" font-weight="600" fill="var(--navy)">
      <text x="15" y="176">0–19</text><text x="15" y="203">20–29</text><text x="15" y="231">30–39</text><text x="15" y="257">40–49</text><text x="15" y="283">50–59</text><text x="15" y="308">60–69</text>
      <text x="15" y="331">70 years</text><text x="15" y="340">and above</text>
    </g>
    <rect x="62" y="168" width="6.6" height="10" fill="var(--blue)"/>
    <rect x="62" y="195" width="70.8" height="10" fill="var(--blue)"/>
    <rect x="62" y="223" width="140.7" height="10" fill="var(--blue)"/>
    <rect x="62" y="249" width="209" height="10" fill="var(--navy)"/>
    <rect x="62" y="275" width="209.9" height="10" fill="var(--navy)"/>
    <rect x="62" y="300" width="110.3" height="10" fill="var(--blue)"/>
    <rect x="62" y="327" width="74" height="10" fill="var(--blue)"/>
    <g font-size="11.5" font-weight="700" fill="var(--navy)">
      <text x="74" y="177">0.8 %</text><text x="138" y="204">8.6 %</text><text x="208" y="232">17.1 %</text>
      <text x="276" y="258">25.4 %</text><text x="277" y="284">25.5 %</text><text x="178" y="309">13.4 %</text><text x="142" y="336">9.0 %</text>
    </g>
  </svg>
  <footer class="footer"><div class="org">CARROWBY<br>INSTITUTE</div><div class="report">Australia’s Yearly Harmwatch Review <b>2026</b></div></footer>
</section>

</body>
</html>
```